Life Coaching business needs a new flyer

We are an Australian business that specialises in Life Coaching, Career Coaching, Health and Wellness Coaching, Yoga and Pilates. We need a A4 double sided flyer that is full colour and folded to DL format. I have attached a couple of designs that I like and some pictures and would like the flyer to be bright yet stylish.

Life Coaching

```html
<!DOCTYPE html>
<html lang="en">
<head>
<meta charset="utf-8">
<title>Clearwater Coaching – Inside Spread</title>
<link href="https://fonts.googleapis.com/css2?family=Open+Sans:wght@400;700&family=Raleway:wght@400;500;700&display=swap" rel="stylesheet">
<style>
  :root{
    --page:#eeeeee;
    --paper:#ffffff;
    --navy:#1b2f5e;
    --brand-blue:#1f8fd3;
    --panel-blue:#0b8dbd;
    --panel-green:#5aac33;
    --logo-green:#3a9a3c;
    --ink:#1d1d1d;
    --white:#ffffff;
  }
  *{box-sizing:border-box;margin:0;padding:0}
  html,body{width:1200px;height:1000px;overflow:hidden;background:var(--page)}
  .spread{position:absolute;left:66px;top:45px;width:1068px;height:823px;background:var(--paper);box-shadow:0 2px 8px rgba(0,0,0,.15);overflow:hidden}
  .block{position:absolute}
  .photo{position:absolute}
  .body-copy{font-family:"Raleway",sans-serif;font-size:11.8px;line-height:14.2px;letter-spacing:-0.1px;color:var(--ink)}
  .heading{font-family:"Open Sans",sans-serif;font-weight:700;font-size:15.5px;line-height:19px}
  .body-copy p+p{margin-top:14px}

  /* panel 1 */
  .sea-photo{left:0;top:0;width:354px;height:413px;background:linear-gradient(160deg,#3fb6c4 0%,#7fd5d6 35%,#a8e4dc 60%,#e9f4ee 100%)}
  .questions{left:18px;top:28px;width:234px;font-family:"Open Sans",sans-serif;font-weight:700;font-size:16px;line-height:21px;letter-spacing:-0.4px;color:var(--navy)}
  .questions p{margin-bottom:20px}
  .team-photo{left:0;top:418px;width:354px;height:184px;background:linear-gradient(180deg,#ffffff 0%,#dfe6ee 60%,#c9d4df 100%)}
  .centre-intro{left:20px;top:607px;width:320px}
  .centre-intro .heading{color:var(--brand-blue);font-size:15px;margin-bottom:2px}

  /* panel 2 */
  .life-coaching{left:373px;top:22px;width:322px}
  .life-coaching .heading{color:var(--brand-blue);margin-bottom:3px}
  .couple-photo{left:354px;top:182px;width:355px;height:216px;background:linear-gradient(120deg,#c89a7a 0%,#e8c9a8 40%,#9fc0cf 70%,#e98a3c 100%)}
  .green-panel{left:354px;top:398px;width:355px;height:245px;background:var(--panel-green);color:var(--white);padding:6px 16px 0 19px}
  .green-panel .body-copy{color:var(--white)}
  .green-panel .section+.section{margin-top:10px}
  .yoga-photo{left:354px;top:643px;width:355px;height:180px;background:linear-gradient(180deg,#1d86c6 0%,#5fb2e0 50%,#eef3f6 75%,#ffffff 100%)}

  /* panel 3 */
  .blue-panel{left:709px;top:0;width:359px;height:525px;background:var(--panel-blue);padding:22px 20px 0 20px;color:var(--white)}
  .blue-panel .body-copy{color:var(--white)}
  .blue-panel .heading{margin-bottom:2px}
  .help-list{list-style:none;margin:10px 0 0 32px;font-family:"Raleway",sans-serif;font-size:13.2px;line-height:19.3px}
  .help-list li{position:relative;padding-left:12px}
  .help-list li::before{content:"";position:absolute;left:0;top:7px;width:5px;height:5px;background:var(--white)}
  .blue-panel .section-med{margin-top:34px}
  .blue-panel .section-yoga{margin-top:24px}
  .brand{left:709px;top:525px;width:359px;height:118px;display:flex;align-items:center;justify-content:center;gap:12px}
  .brand-dot{width:30px;height:30px;border-radius:50%;background:var(--logo-green);flex:none}
  .brand-name{font-family:"Raleway",sans-serif;font-weight:500;font-size:17px;line-height:21px;color:var(--brand-blue)}
  .strip-photo{top:643px;height:180px;width:119px}
  .strip-1{left:709px;background:linear-gradient(180deg,#7cc7e8 0%,#c7e3ee 55%,#d9739a 100%)}
  .strip-2{left:829px;background:linear-gradient(180deg,#f3eee6 0%,#e9b5c2 60%,#b7c59c 100%)}
  .strip-3{left:949px;background:linear-gradient(180deg,#f5d27a 0%,#d8a86e 50%,#8fae5a 100%)}
</style>
</head>
<body>
<main class="spread">
  <!-- panel 1 -->
  <div class="photo sea-photo" role="img" aria-label="Photo of a woman floating on a pink lilo in clear turquoise water"></div>
  <div class="block questions">
    <p>Are you looking at making changes this year?</p>
    <p>Are you stuck in a rut or at a crossroad in your life?</p>
    <p>Are you wanting to lose weigh but can’t get motivated?</p>
    <p>Do you have ongoing problems with your career, relationships, or just life itself?</p>
    <p>Life coaching is the answer</p>
  </div>
  <div class="photo team-photo" role="img" aria-label="Photo of a cheering group of smiling young professionals"></div>
  <section class="block centre-intro">
    <h2 class="heading">Clearwater Coaching and Meditation Centre</h2>
    <div class="body-copy">
      <p>Our mission is to help you become the best possible person you can be. Mentally, physically, and spiritually.</p>
      <p>We offer highly qualified and compassionate trainers/coaches for Life Coaching, Meditation, Yoga and Pilates.<br>They will guide and motivate you every step of the way to achieve all your dreams and goals.</p>
      <p>They will make you be the best you can be J</p>
    </div>
  </section>

  <!-- panel 2 -->
  <section class="block life-coaching">
    <h2 class="heading">Life Coaching</h2>
    <div class="body-copy">
      <p>Your Life Coach will give you the confidence and the ability to move forward in a positive manner in all areas of your life where you crave change.</p>
      <p>Life Coaching is about breaking down the barriers preventing this change from happening, and creating the ideal environment for positive action to take place. It is a holistic approach, which looks at the present and sets goals for a totally successful future.</p>
    </div>
  </section>
  <div class="photo couple-photo" role="img" aria-label="Photo of a smiling older couple toasting with champagne on a boat"></div>
  <div class="block green-panel">
    <section class="section">
      <h2 class="heading">Career Coaching</h2>
      <p class="body-copy">Are you at a crossroads in your career and at a loss about what to do next? Do you want your work to be in alignment with the authentic you? It can be difficult to assess career options, goals, and strategies, and have the confidence to implement changes on your own. With the right coaching support, you will gain the clarity that you need to take control and have a fulfilling and rewarding career.</p>
    </section>
    <section class="section">
      <h2 class="heading">Wellness Coaching</h2>
      <p class="body-copy">Health and wellness coaches help their clients find the motivation and tools to achieve their health and wellness goals, working with the client to examine and improve the psychological framework that supports those goals.</p>
    </section>
  </div>
  <div class="photo yoga-photo" role="img" aria-label="Photo of a woman in white holding a balance yoga pose by the sea"></div>

  <!-- panel 3 -->
  <div class="block blue-panel">
    <section>
      <h2 class="heading">Why Would I Need Help?</h2>
      <p class="body-copy">Coaching is for anyone who wants to make lasting changes in their life. Coaching can assist with such issues as:</p>
      <ul class="help-list">
        <li>Creating a better work- life balance</li>
        <li>Resolving relationship issues</li>
        <li>Career guidance</li>
        <li>Stress management</li>
        <li>Weight loss and fitness</li>
        <li>Motivation and goal setting</li>
        <li>Boosting your self esteem</li>
        <li>Overcoming negative emotions and thoughts</li>
        <li>Better time management</li>
      </ul>
    </section>
    <section class="section-med">
      <h2 class="heading">Meditation</h2>
      <p class="body-copy">We specialise in teaching meditation from beginners to advanced and teach a variety of techniques for stress reduction, peace of mind, stillness, and clarity.</p>
    </section>
    <section class="section-yoga">
      <h2 class="heading">Yoga/Pilates</h2>
      <p class="body-copy">Your highly qualified and experienced Yoga or Pilates instructor will come to you and create a fun and varied workout based on what you enjoy and what your goals are.</p>
    </section>
  </div>
  <div class="block brand">
    <span class="brand-dot"></span>
    <span class="brand-name">Clearwater Coaching<br>and Meditation Centre</span>
  </div>
  <div class="photo strip-photo strip-1" role="img" aria-label="Photo of a joyful woman in a floral dress beside a pink car"></div>
  <div class="photo strip-photo strip-2" role="img" aria-label="Photo of a smiling man with a bowl of salad"></div>
  <div class="photo strip-photo strip-3" role="img" aria-label="Photo of a mother and daughter hugging outdoors"></div>
</main>
</body>
</html>
```